PTA Business Card

Seeking design for a business card, standard size. It is going to be for myself in regards to PTA - details:

Hollis Fernway Elementary School
PTA President
Neil Brawley
555-208-3147
Brawl1984@mailnest.example

Requirement:
Facebook icon? "Hollis Fernway PTA Durn"
Twitter thing? I am new to twitter so not sure what to put, here is the link:
https://chirpline.example/HFRoverbirdsPTA

I was thinking on the front would be a notebook paper background? Not a requirement but was thinking it would look cool?

Total freedom here, let your creativity spread because I don't have any suggestions for design, sorry. Colors of school district are black and yellow.

Backside I am not sure exactly what to put on it.

```html
<!DOCTYPE html>
<html lang="en">
<head>
<meta charset="utf-8">
<title>Hollis Fernway PTA Business Card</title>
<link href="https://fonts.googleapis.com/css2?family=Josefin+Slab:wght@400;500;700&display=swap" rel="stylesheet">
<style>
  :root {
    --stage-light: #12b9e7;
    --stage-mid: #0a5f7a;
    --stage-dark: #020d12;
    --card-yellow: #fff500;
    --card-white: #ffffff;
    --ink: #111111;
    --icon-square: #2b4f8f;
    --icon-square-alt: #1d9bf0;
  }
  * { margin: 0; padding: 0; box-sizing: border-box; }
  html, body { width: 1200px; height: 1000px; overflow: hidden; }
  body {
    position: relative;
    font-family: "Josefin Slab", Georgia, serif;
    color: var(--ink);
    background: radial-gradient(ellipse 1100px 1000px at 200px 130px,
      var(--stage-light) 0%, var(--stage-mid) 50%, var(--stage-dark) 100%);
  }
  .card {
    position: absolute;
    border-radius: 14px;
    box-shadow: -6px 8px 10px rgba(0,0,0,0.45);
  }
  .card--yellow { background: var(--card-yellow); }
  .card--white { background: var(--card-white); }
  .card--front { left: 300px; top: 126px; width: 576px; height: 338px; }
  .card--back-white { left: 15px; top: 493px; width: 574px; height: 337px; }
  .card--back-yellow { left: 611px; top: 493px; width: 575px; height: 337px; }

  .school-name {
    position: absolute;
    left: 0; right: 0;
    text-align: center;
    font-size: 31px;
    font-weight: 500;
    white-space: nowrap;
    letter-spacing: 0.2px;
  }
  .school-name strong { font-weight: 700; }
  .card--front .school-name { top: 150px; }
  .card--back-white .school-name,
  .card--back-yellow .school-name { top: 32px; }

  .contact {
    position: absolute;
    left: 32px;
    top: 165px;
    list-style: none;
    font-size: 19.5px;
    font-weight: 500;
    line-height: 24.2px;
  }
  .contact li { display: flex; align-items: center; white-space: nowrap; }
  .social-mark {
    display: inline-block;
    flex: none;
    width: 18px; height: 18px;
    margin-right: 6px;
    border-radius: 2px;
    background: var(--icon-square);
  }
  .social-mark--alt { background: var(--icon-square-alt); }
</style>
</head>
<body>

  <section class="card card--yellow card--front" aria-label="Card front">
    <h1 class="school-name"><strong>Hollis Fernway</strong> Elementary School</h1>
  </section>

  <section class="card card--white card--back-white" aria-label="Card back, white">
    <h2 class="school-name"><strong>Hollis Fernway</strong> Elementary School</h2>
    <ul class="contact">
      <li>PTA President</li>
      <li>Neil Brawley</li>
      <li>555-208-3147</li>
      <li>Brawl1984@mailnest.example</li>
      <li><span class="social-mark"></span>Hollis Fernway PTA Durn</li>
      <li><span class="social-mark social-mark--alt"></span>https://chirpline.example/HFRoverbirdsPTA</li>
    </ul>
  </section>

  <section class="card card--yellow card--back-yellow" aria-label="Card back, yellow">
    <h2 class="school-name"><strong>Hollis Fernway</strong> Elementary School</h2>
    <ul class="contact">
      <li>PTA President</li>
      <li>Neil Brawley</li>
      <li>555-208-3147</li>
      <li>Brawl1984@mailnest.example</li>
      <li><span class="social-mark"></span>Hollis Fernway PTA Durn</li>
      <li><span class="social-mark social-mark--alt"></span>https://chirpline.example/HFRoverbirdsPTA</li>
    </ul>
  </section>

</body>
</html>
```